"Whole Block Drop" 9x6.5" mailer for church ministry event in park

We are a small church trying to reach out in a relevant way to our community. We want to send a postcard ad to all the houses on the surrounding mail routes via "Whole Block Drop" (see CCAmailhub.com for more info or I can provide specs if you do not already have them). Mailer actually needs to be at least 6.25" high. 9x6.5 is the biggest we want to go. Attached docs should provide all the necessary info. Front side of card will have necessary postal stuff in top right and rest should be devoted to our "Main Event" which is the event in the park (see attached info). 2nd biggest event to highlight (front or back) is our Sunbeam Story Circle. Our goal is to target families with young kids and encourage them to visit our church for one of these events and want to come back again! Our church website is www.ellwoodvine.com. We are a growing family-friendly local church that wants to "help families grow." I have also considered the tag line "helping to make our community more pleasant" because we live in Pleasant Township. I look forward to seeing your ideas!

Target Market(s)

Families with young children in our local community

Industry/Entity Type

Religious

Requirements
Must have
• Crestline Courier Agency requirements for "Whole Block Drop" mailing (ccamailhub.com); highlight main event on front (plus one more event if space allows); summer "calendar of events on back side plus information about our local church to attract "unchurched" families

```html
<!DOCTYPE html>
<html lang="en">
<head>
<meta charset="utf-8">
<title>Family Fun Mailer – Ellwood Vine</title>
<link rel="stylesheet" href="https://fonts.googleapis.com/css2?family=Source+Sans+3:ital,wght@0,400;0,600;0,700;1,400&family=Noticia+Text:ital@1&family=Marcellus+SC&family=Arimo:wght@400;700&display=swap">
<style>
  :root {
    --page: #e9e7e3;
    --cream: #f7f6df;
    --band-yellow: #f2f0a3;
    --orange: #ef5a2c;
    --red: #e2222b;
    --blue: #1766b2;
    --ink: #1b1b1b;
    --sun: #f5e93a;
    --grey-text: #555;
  }
  html, body {
    margin: 0;
    width: 1053px;
    height: 1200px;
    overflow: hidden;
    background: var(--page);
  }
  .mailer-side {
    position: absolute;
    width: 714px;
    height: 483px;
    box-shadow: 0 6px 14px rgba(0,0,0,.25);
    background: #fff;
  }
  .mailer-side svg { display: block; width: 100%; height: 100%; }
  .front { left: 86px; top: 56px; }
  .back { left: 179px; top: 602px; }
  .sans { font-family: "Source Sans 3", sans-serif; }
  .serif-italic { font-family: "Noticia Text", serif; font-style: italic; }
  .caps { font-family: "Marcellus SC", serif; }
  .postal { font-family: "Arimo", sans-serif; }
</style>
</head>
<body>

<section class="mailer-side front" aria-label="Mailer front">
  <svg viewBox="0 0 893 603" xmlns="http://www.w3.org/2000/svg">
    <defs>
      <radialGradient id="sunburst" cx="0.72" cy="0.35" r="0.7">
        <stop offset="0" stop-color="#fbfbea"/>
        <stop offset="1" stop-color="var(--cream)"/>
      </radialGradient>
      <linearGradient id="photo-tones" x1="0" y1="0" x2="1" y2="1">
        <stop offset="0" stop-color="#6f8f4a"/>
        <stop offset="0.45" stop-color="#a9b890"/>
        <stop offset="0.75" stop-color="#c9a7b4"/>
        <stop offset="1" stop-color="#5d86b5"/>
      </linearGradient>
      <linearGradient id="bounce-tones" x1="0" y1="0" x2="0" y2="1">
        <stop offset="0" stop-color="#e8eef5"/>
        <stop offset="0.5" stop-color="#c23a3a"/>
        <stop offset="1" stop-color="#3a4fa8"/>
      </linearGradient>
    </defs>

    <rect class="card-ground" width="893" height="603" fill="url(#sunburst)"/>

    <!-- family photo area with curved edge -->
    <path d="M0,0 H352 C432,90 432,270 318,360 L0,385 Z" fill="url(#photo-tones)" role="img" aria-label="Photo of a smiling family walking outdoors with a child on the father's shoulders"/>
    <path class="edge-orange" d="M352,0 C432,90 432,270 318,360" fill="none" stroke="var(--orange)" stroke-width="16"/>
    <path class="edge-yellow" d="M372,0 C452,92 448,280 330,372" fill="none" stroke="var(--sun)" stroke-width="5"/>

    <!-- event band -->
    <rect class="event-band" x="380" y="333" width="513" height="154" fill="var(--band-yellow)"/>

    <!-- orange corner block -->
    <path d="M0,382 C130,360 230,372 318,410 L530,603 H0 Z" fill="var(--orange)"/>
    <path d="M0,382 C130,360 230,372 318,410 L530,603" fill="none" stroke="var(--ink)" stroke-width="6"/>

    <!-- bounce house -->
    <circle cx="305" cy="440" r="84" fill="url(#bounce-tones)" role="img" aria-label="Inflatable bounce castle"/>
    <circle cx="305" cy="440" r="84" fill="none" stroke="var(--blue)" stroke-width="6"/>

    <!-- event title lettering -->
    <rect x="478" y="22" width="300" height="210" rx="30" fill="#eeeccd" role="img" aria-label="Hand-lettered Family Fun event title in black, yellow, blue and red"/>

    <text class="sans" x="645" y="282" text-anchor="middle" font-size="21" fill="var(--red)">HELPING TO MAKE OUR COMMUNITY</text>
    <text class="sans" x="645" y="308" text-anchor="middle" font-size="21" fill="var(--red)">MORE PLEASANT</text>

    <g class="sans" text-anchor="middle">
      <text x="517" y="384" font-size="27" font-weight="700" fill="var(--red)">PLEASANT PARK</text>
      <text x="517" y="417" font-size="25" font-weight="600" fill="var(--ink)">Sunday June 26</text>
      <text x="517" y="450" font-size="25" font-weight="600" fill="var(--ink)">4:00 - 8:30pm</text>
      <text x="757" y="384" font-size="27" font-weight="700" fill="var(--red)">BIRCHWOOD PARK</text>
      <text x="757" y="417" font-size="25" font-weight="600" fill="var(--ink)">Monday June 27</text>
      <text x="757" y="450" font-size="25" font-weight="600" fill="var(--ink)">4:00 - 8:30pm</text>
    </g>

    <g class="serif-italic" fill="#fff" font-size="36">
      <text x="34" y="438">Food</text>
      <text x="34" y="484">Games</text>
      <text x="34" y="528">Fun!</text>
    </g>
    <text class="serif-italic" x="34" y="586" font-size="33" fill="var(--sun)">Prizes • Music • More!</text>

    <text class="sans" x="637" y="576" text-anchor="middle" font-size="19" font-style="italic" fill="var(--ink)">with special guests</text>
    <g class="guest-name">
      <rect x="742" y="513" width="124" height="70" fill="#fff"/>
      <rect x="748" y="539" width="16" height="16" fill="var(--blue)"/>
      <text class="sans" x="770" y="537" font-size="17" font-weight="700" fill="var(--blue)">OPEN</text>
      <text class="sans" x="770" y="556" font-size="17" font-weight="700" fill="var(--blue)">HARBOR</text>
      <text class="sans" x="770" y="575" font-size="17" font-weight="700" fill="var(--blue)">CREW</text>
    </g>
  </svg>
</section>

<section class="mailer-side back" aria-label="Mailer back">
  <svg viewBox="0 0 893 604" xmlns="http://www.w3.org/2000/svg">
    <defs>
      <linearGradient id="top-grey" x1="0" y1="0" x2="0" y2="1">
        <stop offset="0" stop-color="#f6f6f6"/>
        <stop offset="1" stop-color="#d9dadb"/>
      </linearGradient>
      <clipPath id="panel-clip">
        <path d="M0,0 H430 C492,180 492,400 425,604 H0 Z"/>
      </clipPath>
    </defs>

    <rect width="893" height="604" fill="#fff"/>

    <path class="edge-orange" d="M436,0 C500,180 500,400 432,604" fill="none" stroke="var(--orange)" stroke-width="18"/>

    <g clip-path="url(#panel-clip)">
      <rect width="500" height="174" fill="url(#top-grey)"/>
      <rect y="174" width="500" height="74" fill="var(--blue)"/>
      <rect y="248" width="500" height="272" fill="var(--orange)"/>
      <rect y="520" width="500" height="84" fill="var(--band-yellow)"/>
    </g>

    <rect x="102" y="26" width="240" height="144" rx="12" fill="#e6e6e6" role="img" aria-label="Line drawing of a family with children and a pet dog"/>

    <text class="caps" x="232" y="223" text-anchor="middle" font-size="36" fill="#fff">Family Fun Events</text>

    <g class="sans" fill="#fff" text-anchor="middle">
      <text x="222" y="282" font-size="19" font-weight="700">June 26</text>
      <text x="222" y="303" font-size="19">Pleasant Park w/ Open Harbor Crew</text>
      <text x="222" y="330" font-size="19" font-weight="700">June 27</text>
      <text x="222" y="351" font-size="19">Birchwood Park w/ Open Harbor Crew</text>
      <text x="222" y="378" font-size="19" font-weight="700">July 12</text>
      <text x="222" y="399" font-size="19">Academy of Arts @ Ellwood Vine</text>
      <text x="222" y="426" font-size="19" font-weight="700">July 31</text>
      <text x="222" y="447" font-size="19">Sunbeam Story Circle “Opening Ceremony”</text>
      <text x="222" y="475" font-size="19" font-weight="700">August 11</text>
      <text x="222" y="496" font-size="19">Gearhouse Men’s Group “Car Show”</text>
    </g>

    <text class="serif-italic" x="20" y="560" font-size="21" fill="var(--ink)">Bring your family@ Ellwood Vine</text>

    <circle cx="478" cy="310" r="80" fill="var(--band-yellow)" stroke="#dcdcdc" stroke-width="6"/>
    <g class="serif-italic" text-anchor="middle" font-size="17" fill="var(--ink)">
      <text x="478" y="294">INVITE YOUR</text>
      <text x="478" y="316">FRIENDS!!</text>
      <text x="478" y="338">Please pray!</text>
    </g>

    <g class="sans" fill="var(--grey-text)" font-size="16">
      <text x="494" y="41" fill="var(--ink)">Ellwood Vine</text>
      <text x="494" y="67">418 Larkspur Ln, Dunmore,</text>
      <text x="494" y="85">OH 43399</text>
      <text x="494" y="104">(740) 555-0148</text>
      <text x="494" y="122">www.ellwoodvine.com</text>
    </g>

    <g class="postal" font-size="9" text-anchor="middle" fill="var(--ink)">
      <rect x="784" y="28" width="72" height="69" fill="none" stroke="#444" stroke-width="1"/>
      <text x="820" y="42">PRSRT STD</text>
      <text x="820" y="53">ECRWSS</text>
      <text x="820" y="65">U.S. Postage</text>
      <text x="820" y="76" font-weight="700">PAID</text>
      <text x="820" y="88">WBD RETAIL</text>
    </g>

    <g class="postal" fill="var(--ink)">
      <rect x="619" y="206" width="241" height="95" fill="none" stroke="#444" stroke-width="1"/>
      <text x="690" y="229" font-size="11">****************ECRWSS****</text>
      <text x="636" y="264" font-size="13">Local</text>
      <text x="636" y="281" font-size="13">Postal Customer</text>
    </g>
  </svg>
</section>

</body>
</html>
```